Webdesign für Beratung von Firmen zum Thema Radon
Zielgruppe
Firmenname: Lumivelde - Ich informiere und berate als Radon Fachperson, Privatpersonen sowie Firmen zum Thema Radon, und die Gefahren die damit verbunden sind in bestehenden Gebäuden und Neubauten. Die Leistung erfolgt in Form eines ausgearbeiteten Sanierungskonzeptes bzw. bautechnische Maßnahmen beim Neubau.
Aufgabenstellung
Keep it simple and clean, weniger ist mehr. Die beigefügten Info-Grafiken sollen nur als Information dienen zum Thema Radon, und sollen nicht verwendet werden - ich hoffe hier doch besseres Bildmaterial von euch zu bekommen :-)

```html
<!DOCTYPE html>
<html lang="de">
<head>
<meta charset="utf-8">
<title>Lumivelde – Radon Beratung</title>
<link href="https://fonts.googleapis.com/css2?family=Source+Sans+3:wght@400;600;700&family=Work+Sans:wght@400;600;700&display=swap" rel="stylesheet">
<style>
:root{
  --blue:#1f63a1;
  --dark:#202020;
  --white:#ffffff;
  --green:#34a033;
  --green-dark:#2a8a2a;
  --text-dark:#222222;
  --field:#f4f4f4;
}
*{box-sizing:border-box;margin:0;padding:0}
html,body{width:1200px;height:3460px;overflow:hidden}
body{position:relative;background:var(--white);font-family:"Source Sans 3",sans-serif;color:var(--white)}
.abs{position:absolute}
/* header */
.site-header{left:0;top:0;width:1200px;height:108px;background:var(--white)}
.brand{left:94px;top:38px;display:flex;align-items:center;gap:8px;font-size:22px;font-weight:700;color:var(--green-dark)}
.brand-dot{width:14px;height:14px;border-radius:50%;background:var(--green)}
.nav a{position:absolute;top:42px;font-size:18px;color:var(--text-dark);text-decoration:none}
/* sections */
.band{left:0;width:1200px}
.experts{top:108px;height:528px;background:var(--blue)}
.radon{top:649px;height:819px;background:var(--dark)}
.services{top:1481px;height:1267px;background:var(--blue)}
.contact{top:2763px;height:609px;background:var(--dark)}
.site-footer{top:3381px;height:79px;background:var(--dark)}
.section-title{font-weight:700;font-size:50px;line-height:1}
.services .section-title{font-family:"Work Sans",sans-serif;font-size:49px}
/* expert cards */
.expert-card{width:421px;height:415px;background:var(--white);border-radius:22px;top:195px;box-shadow:0 4px 10px rgba(0,0,0,.25)}
.expert-photo{left:12px;top:11px;width:235px;height:395px;border-radius:24px;
  background:radial-gradient(ellipse 60% 45% at 52% 48%,#efc7aa 0%,#e2b48f 35%,#d2a76a 60%,rgba(210,167,106,0) 80%),
             radial-gradient(ellipse 80% 70% at 50% 45%,#c99a58 0%,#b08a55 55%,rgba(176,138,85,0) 85%),
             linear-gradient(180deg,#e7e7e4 0%,#d9d7d2 70%,#8fa8b8 100%)}
.expert-name{left:258px;top:12px;font-size:23px;line-height:30px;color:var(--text-dark)}
.expert-bio{left:258px;top:72px;width:152px;font-size:15.5px;line-height:20px;color:var(--text-dark)}
/* radon */
.radon-img{left:87px;width:421px;border-radius:20px}
.radon-house{top:761px;height:359px;
  background:radial-gradient(ellipse 45% 40% at 58% 40%,#c9ccd1 0%,#dfe1e4 55%,rgba(223,225,228,0) 80%),
             linear-gradient(160deg,#f7f8f9 0%,#eceef0 55%,#dcdfe3 100%)}
.radon-table{top:1173px;height:264px;
  background:radial-gradient(circle at 76% 48%,#b4b0a8 0%,#7d7a74 9%,#4c4a47 17%,rgba(76,74,71,0) 24%),
             linear-gradient(170deg,#5a5a5a 0%,#6a6a6a 45%,#474747 100%)}
.faq{left:691px;top:762px;width:414px}
.faq h3{font-size:18px;font-weight:600;line-height:22px}
.faq p{font-size:15px;line-height:20px;margin-bottom:22px;color:#f0f0f0}
.cta{left:693px;top:1379px;width:327px;height:54px;border-radius:27px;background:var(--green);border:2px solid var(--green-dark);font-size:30px;font-weight:700;display:flex;align-items:center;justify-content:center;color:var(--white)}
/* services */
.services-intro{left:87px;top:1594px;width:1080px;font-family:"Work Sans",sans-serif;font-size:15px;line-height:19px}
.services-intro h3{font-size:20px;font-weight:600;margin-bottom:22px}
.services-intro .step{font-size:18px;font-weight:600;line-height:20px}
.services-intro p{margin-bottom:18px}
.services-intro b{font-weight:600}
.services-intro h4{font-size:21px;font-weight:600;margin-top:26px}
.project{width:593px;height:237px;background:var(--dark);border-radius:24px}
.project-photo{top:26px;width:236px;height:186px;border-radius:24px}
.photo-family{background:linear-gradient(180deg,#8cc0ea 0%,#b7d3ea 22%,#a9503f 40%,#c47060 55%,#e9e6dc 68%,#7aa74c 82%,#5f9038 100%)}
.photo-villa{background:radial-gradient(ellipse 45% 35% at 55% 50%,#e8b97a 0%,#a9825a 45%,rgba(169,130,90,0) 80%),
             linear-gradient(180deg,#2f4f8f 0%,#5b79b3 35%,#6f6a64 62%,#3a3a36 100%)}
.project-text{top:26px;font-size:15px;line-height:20px}
.project-text strong{display:block;font-size:21px;font-weight:600;line-height:27px}
.project-text em{display:block;font-style:normal;font-size:18px;font-weight:600;line-height:23px}
/* contact */
.contact-sub{left:87px;top:2865px;font-size:21px;font-weight:600}
.field{background:var(--field);border:2px solid #cfcfcf;color:#666;font-size:21px;padding:2px 6px}
.send{left:87px;top:3311px;width:162px;height:39px;background:var(--green);border-radius:4px;font-size:21px;font-weight:600;display:flex;align-items:center;justify-content:center}
.footer-link{top:3410px;font-size:19px;font-weight:700;color:var(--white);text-decoration:none}
.divider{left:0;width:1200px;height:13px;background:var(--white)}
</style>
</head>
<body>

<header class="abs site-header">
  <div class="abs brand"><span class="brand-dot"></span>Lumivelde</div>
  <nav class="nav">
    <a style="left:347px">Über uns</a>
    <a style="left:493px">Gefahren durch Radon</a>
    <a style="left:765px">Leistungen/Referenzen</a>
    <a style="left:1042px">Kontakt</a>
  </nav>
</header>

<section class="abs band experts">
  <h2 class="abs section-title" style="left:89px;top:20px">Unsere Experten</h2>
</section>
<article class="abs expert-card" style="left:89px">
  <div class="abs expert-photo" role="img" aria-label="Porträtfoto einer blonden Expertin"></div>
  <div class="abs expert-name">Berta<br>Beispiel</div>
  <p class="abs expert-bio">Lorem ipsum dolor sit amet, consetetur sadipscing elitr, sed diam nonumvy eirmod tempor invidunt ut labore et dolore magna aliquyam erat, sed diam voluptua. At vero eos et accusam et justo duo dolores et ea rebum. Stet clita kasd gubergren, no sea takimata sanctus est.</p>
</article>
<article class="abs expert-card" style="left:692px">
  <div class="abs expert-photo" role="img" aria-label="Porträtfoto einer blonden Expertin"></div>
  <div class="abs expert-name">Berta<br>Beispiel</div>
  <p class="abs expert-bio">Lorem ipsum dolor sit amet, consetetur sadipscing elitr, sed diam nonumvy eirmod tempor invidunt ut labore et dolore magna aliquyam erat, sed diam voluptua. At vero eos et accusam et justo duo dolores et ea rebum. Stet clita kasd gubergren, no sea takimata sanctus est.</p>
</article>

<div class="abs divider" style="top:636px"></div>

<section class="abs band radon">
  <h2 class="abs section-title" style="left:94px;top:30px">Gefahren durch Radon</h2>
</section>
<div class="abs radon-img radon-house" role="img" aria-label="Illustration eines Hauses im Querschnitt, in das Radon aus dem Boden eindringt"></div>
<div class="abs radon-img radon-table" role="img" aria-label="Periodensystem mit hervorgehobenem Element Radon als silberne Kugel"></div>
<div class="abs faq">
  <h3>Was ist Radon?</h3>
  <p>Radon ist ein radioaktives Gas, welches im Boden entsteht. Für den Menschen ist es gefährlich, denn es ist krebserregend: Radon ist laut der University of Westbrook die zweithäufigste Ursache für Lungenkrebs.</p>
  <h3>Was passiert mit dem Radon?</h3>
  <p>Das Radon gelangt durch durchlässige Böden und Fundamente in Kellerräume und letztendlich auch in Wohnräume. Die Radonkonzentration steigt. Radon-Moleküle setzen sich an Partikel wie Staub oder Tabakrauch fest. Zusammen mit diesen Partikel gelangt Radon in die Lunge und richtet dort Schaden an. (Passiv-)Raucher-Haushalte sind also besonders gefährdet.</p>
  <h3>Ist jede Region gleich stark betroffen?</h3>
  <p>Nein. Die Belastung ist sogar lokal unterschiedlich, weshalb die tatsächliche Belastung nur durch professionelle Messungen festgestellt werden kann.</p>
  <h3>Wie kann ich mich schützen?</h3>
  <p>Wir beraten Sie individuell, um für Sie eine ideale und individuelle Lösung finden zu können. Wir greifen hier auf unser Fachwissen und unsere Erfahrung zurück.</p>
  <h3>Sind Neubauten betroffen?</h3>
  <p>Ja, auch Neubauten sind ohne entsprechenden Schutz gefährdet. Auch in diesem Bereich beraten wir Sie gerne.</p>
</div>
<a class="abs cta">Jetzt anfragen</a>

<div class="abs divider" style="top:1468px"></div>

<section class="abs band services">
  <h2 class="abs section-title" style="left:87px;top:28px">Leistungen/Referenzen</h2>
</section>
<div class="abs services-intro">
  <h3>So schützen wir ihre Gesundheit:</h3>
  <div class="step">Erste Stufe</div>
  <p><b>Wir begutachten Ihr Objekt</b> und <b>beraten Sie umfassend</b>. Hierbei profitieren Sie von unserer <b>Expertise</b>.</p>
  <div class="step">Zweite Stufe</div>
  <p><b>Wir sanieren Ihr Objekt</b>. So ist sichergestellt, dass Sie in Zukunft <b>ohne gesundheitsschädliche Radon-Belastung leben</b> können.</p>
  <h4>Wir haben Ihnen folgend einige unserer Referenzen aufgelistet:</h4>
</div>

<article class="abs project" style="left:87px;top:1824px">
  <div class="abs project-photo photo-family" style="left:13px" role="img" aria-label="Familie läuft vor ihrem roten Holzhaus über die Wiese"></div>
  <div class="abs project-text" style="left:260px"><strong>Projekt 1</strong><em>Projektbeschreibung</em>- Besonderheit 1<br>- Besonderheit 2<br>- Besonderheit 3</div>
</article>
<article class="abs project" style="left:519px;top:2161px">
  <div class="abs project-photo photo-villa" style="left:344px" role="img" aria-label="Beleuchtetes modernes Haus in der Abenddämmerung"></div>
  <div class="abs project-text" style="right:259px;text-align:right"><strong>Projekt 2</strong><em>Projektbeschreibung</em>- Besonderheit 1<br>- Besonderheit 2<br>- Besonderheit 3</div>
</article>
<article class="abs project" style="left:87px;top:2486px">
  <div class="abs project-photo photo-family" style="left:13px" role="img" aria-label="Familie läuft vor ihrem roten Holzhaus über die Wiese"></div>
  <div class="abs project-text" style="left:260px"><strong>Projekt 1</strong><em>Projektbeschreibung</em>- Besonderheit 1<br>- Besonderheit 2<br>- Besonderheit 3</div>
</article>

<div class="abs divider" style="top:2748px;height:15px"></div>

<section class="abs band contact">
  <h2 class="abs section-title" style="left:87px;top:20px">Kontaktieren Sie uns</h2>
</section>
<div class="abs contact-sub">Wir erstellen Ihnen gerne ein individuelles Angebot</div>
<div class="abs field" style="left:87px;top:2912px;width:335px;height:39px">Vorname</div>
<div class="abs field" style="left:433px;top:2912px;width:334px;height:39px">Nachname</div>
<div class="abs field" style="left:87px;top:2978px;width:335px;height:38px">E-Mail-Adresse</div>
<div class="abs field" style="left:87px;top:3043px;width:593px;height:242px">Ihre Anfrage</div>
<div class="abs send">Abschicken</div>

<div class="abs divider" style="top:3372px;height:9px"></div>
<footer class="abs band site-footer"></footer>
<a class="abs footer-link" style="left:751px">Impressum</a>
<a class="abs footer-link" style="left:997px">Datenschutz</a>

</body>
</html>
```